Tri-fold two sided brochure for Maplebrook Ridge Home Health Care
Maplebrook Ridge Home Health Care
Tri-fold two sided brochure for Maplebrook Ridge Home Health Care - Medical
Creative Brief
Medical
Maplebrook Ridge Home Health is a full service home health agency, providing a wide range of skilled and supportive services including: Wound Care, Ostomy Care, Catheter Care, pre and post-Op Care, Medication Management, Diabetic Management, Patient and care giver training, Pain Management, Feeding Tubes, Intramuscular Injections, Subcutaneous Injections, Nutritional Counselling, Disease Management, Blood pressure Monitoring, PT/INR Monitoring, Blood Draw and IV Therapy. Our Services are as follows: Skilled Nursing Physical Therapy Occupational Therapy Speech Therapy Home health Aide Medical Social Worker Registered Dietitian
on the first page I want the logo with black or white background and a picture on the back I want pictures, address and contact numbers In the middle I want the content and the services we provide I need help with the pictures and content I just wrote some in the detail and target boxes some ideas Our target is patients who are in need of home health care but mainly their physicians are the target because patients need to get the referrals from their primary physicians, medicare and insurance companies
tulipgate42 tulipgate42
I would like the unified accreditation board logo on the first page please

```html
<!DOCTYPE html>
<html lang="en">
<head>
<meta charset="utf-8">
<title>Maplebrook Ridge Home Health Care – Brochure Inside Spread</title>
<link rel="stylesheet" href="https://fonts.googleapis.com/css2?family=Montserrat:wght@600;700&family=Open+Sans:wght@400;600&display=swap">
<style>
  :root{
    --teal:#1b8d84;
    --teal-dark:#137168;
    --ink:#4a4a4a;
    --muted:#8a8a8a;
    --rule:#d6d6d6;
    --paper:#ffffff;
    --panel-grey:#f1f1f1;
    --backdrop:#e6e6e6;
    --photo-a:#c9b8a6;
    --photo-b:#7fa8b3;
  }
  *{box-sizing:border-box;margin:0;padding:0}
  html,body{width:1200px;height:1080px;overflow:hidden;background:var(--backdrop)}
  body{position:relative;font-family:"Open Sans",Arial,sans-serif;color:var(--ink)}

  .brochure{position:absolute;left:30px;top:140px;width:1140px;height:800px;background:var(--paper);box-shadow:0 6px 24px rgba(0,0,0,.12)}
  .panel{position:absolute;top:0;height:800px;width:380px}
  .panel--about{left:0}
  .panel--services{left:380px;border-left:1px solid #eeeeee}
  .panel--contact{left:760px;background:var(--panel-grey);border-left:1px solid #e2e2e2;border-bottom:6px solid var(--teal)}

  .hero{position:absolute;left:0;top:0;width:760px;height:370px;overflow:hidden;
        background:linear-gradient(110deg,var(--photo-a) 0%,#d9cdbf 40%,#a9c2c6 65%,var(--photo-b) 100%)}
  .hero svg{position:absolute;left:0;top:0}

  .about-copy{position:absolute;left:0;top:380px;width:380px;padding:0 34px}
  .section-title{font-family:"Montserrat",Arial,sans-serif;font-weight:700;font-size:26px;letter-spacing:.5px;color:var(--teal);margin:8px 0 14px}
  .about-copy p{font-size:13px;line-height:1.6;color:var(--muted);margin-bottom:16px}

  .services{position:absolute;left:0;top:370px;width:380px}
  .services__bar{height:56px;background:var(--teal);color:#fff;display:flex;align-items:center;padding-left:22px;
                 font-family:"Montserrat",Arial,sans-serif;font-weight:700;font-size:24px;letter-spacing:.5px}
  .services__list{list-style:none;margin-top:10px}
  .services__item{display:flex;height:44px;align-items:stretch}
  .services__num{width:40px;background:var(--teal);color:#fff;font-size:13px;display:flex;align-items:center;justify-content:center;border-bottom:1px solid rgba(255,255,255,.35)}
  .services__name{flex:1;margin:0 30px 0 18px;display:flex;align-items:center;font-size:14px;color:var(--muted);border-bottom:1px solid var(--rule)}

  .contact{position:absolute;left:0;top:210px;width:380px;padding:0 56px}
  .contact .section-title{text-align:center;margin-bottom:12px}
  .contact__rule{height:1px;background:var(--rule);margin:0 0 22px}
  .contact__lines{font-size:12.5px;line-height:1.75;color:var(--muted);margin-bottom:22px}
  .contact__lines span{color:var(--ink);font-weight:600}
</style>
</head>
<body>
  <div class="brochure">
    <div class="hero" role="img" aria-label="Photo of a caregiver smiling with an elderly patient at home">
      <svg width="760" height="370" viewBox="0 0 760 370" aria-hidden="true">
        <polygon points="0,0 760,0 760,140 380,18 0,140" fill="var(--teal)"/>
        <polygon points="0,140 380,18 760,140 760,150 380,32 0,150" fill="#ffffff"/>
        <polygon points="0,260 200,370 0,370" fill="#ffffff"/>
      </svg>
    </div>

    <section class="panel panel--about">
      <div class="about-copy">
        <h2 class="section-title">WHO WE ARE ?</h2>
        <p>We bring skilled, caring support into the homes of patients across our region. Our nurses and therapists work closely with physicians to build a plan that fits each person, helping them heal, stay safe and keep their independence at home.</p>
        <p>Every visit is guided by clear goals and regular updates to the referring doctor. From wound care to medication management, our team delivers care you can trust, close to family.</p>
      </div>
    </section>

    <section class="panel panel--services">
      <div class="services">
        <h2 class="services__bar">OUR SERVICES</h2>
        <ol class="services__list">
          <li class="services__item"><span class="services__num">1</span><span class="services__name">Skilled Nursing</span></li>
          <li class="services__item"><span class="services__num">2</span><span class="services__name">Physical Therapy</span></li>
          <li class="services__item"><span class="services__num">3</span><span class="services__name">Occupational Therapy</span></li>
          <li class="services__item"><span class="services__num">4</span><span class="services__name">Speech Therapy</span></li>
          <li class="services__item"><span class="services__num">5</span><span class="services__name">Home Health Aide</span></li>
          <li class="services__item"><span class="services__num">6</span><span class="services__name">Medical Social Worker</span></li>
          <li class="services__item"><span class="services__num">7</span><span class="services__name">Registered Dietitian</span></li>
        </ol>
      </div>
    </section>

    <section class="panel panel--contact">
      <div class="contact">
        <h2 class="section-title">CONTACT US</h2>
        <div class="contact__rule"></div>
        <div class="contact__lines">
          <div><span>Tel:</span> (555) 318-2460</div>
          <div><span>Fax:</span> (555) 318-2461</div>
          <div><span>Toll Free:</span> (800) 555-0174</div>
        </div>
        <div class="contact__lines">
          <div><span>Email:</span> info@maplebrookridgehomehealth.com</div>
        </div>
        <div class="contact__lines">
          <div>4120 Alder Creek Road, Suite 210</div>
          <div>Fairhaven, CA 90000</div>
        </div>
        <div class="contact__rule"></div>
      </div>
    </section>
  </div>
</body>
</html>
```